Photobook template design

Just one book of 4/5 pages needed to find a handful of designers to help with this project that will be ongoing for several months, we will agree design price per book.

Hi there, we need lots of fabulous photobook templates designed:
there will be 20 books to start with, canvas layouts, calendar layouts etc.

The MAIN idea of the template is to facilitate the easiest creation / ordering of photobooks etc. possible for the client, so all they have to do is upload their pics and drop them into the templates you're going to design...

Each photobook needs to have min 20 pages, there can be a common theme throughout, but they must be different enough so that they do not all blend into one.
Choose to create a design from the following categories:
family
kids
travel
romance / love
seasonal holiday
year in review
everyday / general
recipes
pets / animals
collage
scrapbook

the quality and look and feel must be equal to www.pagelark.com / www.snapvellum.com / www.printorra.co.uk

In order to keep the designs as fresh as possible - we will work with several designers, so for this first project we will choose 1 designer, but then we'll create other design projects for which you will be specifically invited to design for - it's the only way the do multiple designs/projects.

please see 2 pics attached of other templates already designed - we're very happy with these...

Target Market(s)

These photobooks / calendars / canvas prints are for the average family - not too serious, must be fun / tongue in cheek etc.
They're for people who want to do photobooks but have no clue or do not have the time - so they must LOVE the design, and then want to just add their photos...

Industry/Entity Type

Travel

Requirements
Must have
• Must be designed in Layoutra or Vectorix.
Metric sizes please - Either A3 landscape or portrait with 3 mm bleed, or 300 x 300mm square - 3mm bleed
If you place photos for proofing, please use imagewell images - we have a imagewell account

```html
<!DOCTYPE html>
<html lang="en">
<head>
<meta charset="utf-8">
<title>Travel Album – Photobook Spread</title>
<link rel="stylesheet" href="https://fonts.googleapis.com/css2?family=Arimo&family=Crimson+Text:ital@1&family=Pinyon+Script&display=swap">
<style>
  :root {
    --backdrop: #e6e3de;
    --page-light: #ededed;
    --panel-green: #28322a;
    --ink-dark: #2a2a2a;
    --ornament: #2c3a2e;
    --strip-black: #1f1f1f;
    --text-light: #ffffff;
    --sunset-sky: #e9d3b0;
    --sunset-glow: #f4c27a;
    --sunset-sand: #a8703a;
    --sea-teal: #53b8c2;
    --sea-deep: #2f8fa0;
    --photo-girl: #6fa88a;
    --photo-woman: #b9d3e4;
    --photo-couple: #8fb0c6;
  }

  * { box-sizing: border-box; margin: 0; padding: 0; }

  html, body {
    width: 1200px;
    height: 878px;
    overflow: hidden;
    background: var(--backdrop);
  }

  .spread {
    position: absolute;
    left: 50px;
    top: 50px;
    width: 1100px;
    height: 778px;
  }

  /* Left page */
  .page-left {
    position: absolute;
    left: 0; top: 0;
    width: 550px; height: 778px;
  }

  .hero-photo {
    position: absolute;
    left: 0; top: 0;
    width: 550px; height: 552px;
    background:
      radial-gradient(circle at 48% 40%, var(--sunset-glow) 0%, rgba(244,194,122,0) 40%),
      linear-gradient(180deg, #9fb8cc 0%, var(--sunset-sky) 42%, #c9a06a 55%, var(--sunset-sand) 75%, #5a3a1e 100%);
  }

  .story-panel {
    position: absolute;
    left: 0; top: 552px;
    width: 550px; height: 226px;
    background: var(--panel-green);
  }

  .story-text {
    position: absolute;
    left: 47px; top: 48px;
    width: 444px;
    font-family: "Arimo", Arial, sans-serif;
    font-size: 11px;
    line-height: 17.8px;
    color: var(--text-light);
    white-space: nowrap;
  }

  .story-line {
    display: block;
    text-align: justify;
    text-align-last: justify;
  }

  .story-line--last {
    text-align: left;
    text-align-last: left;
  }

  /* Right page */
  .page-right {
    position: absolute;
    left: 550px; top: 0;
    width: 550px; height: 778px;
    background: var(--page-light);
    overflow: hidden;
  }

  .scenery-photo {
    position: absolute;
    left: 0; top: 330px;
    width: 550px; height: 448px;
    background:
      linear-gradient(180deg, rgba(237,237,237,1) 0%, rgba(237,237,237,0) 35%),
      linear-gradient(180deg, #cfe3e6 0%, var(--sea-teal) 55%, var(--sea-deep) 100%);
  }

  .album-title {
    position: absolute;
    left: 0; top: 92px;
    width: 550px;
    text-align: center;
    font-family: "Pinyon Script", cursive;
    font-weight: 400;
    font-size: 42px;
    line-height: 1;
    color: var(--ink-dark);
  }

  .title-rules {
    position: absolute;
    left: 162px; top: 80px;
  }

  .section-rule {
    position: absolute;
    left: 183px;
  }
  .section-rule--top { top: 240px; }
  .section-rule--bottom { top: 549px; }

  .photo-strip {
    position: absolute;
    left: 65px; top: 255px;
    width: 485px; height: 290px;
    background: var(--strip-black);
  }

  .strip-photo {
    position: absolute;
    top: 13px;
    height: 263px;
  }
  .strip-photo--girl   { left: 2px;   width: 206px; background: linear-gradient(160deg, #9ccf8a, var(--photo-girl) 55%, #2f7f8f); }
  .strip-photo--woman  { left: 216px; width: 135px; background: linear-gradient(180deg, var(--photo-woman), #e8eef2 60%, #6e9a62); }
  .strip-photo--couple { left: 358px; width: 127px; background: linear-gradient(180deg, var(--photo-couple), #b8a27c 70%, #c89a62); }

  .caption {
    position: absolute;
    right: 12px; top: 674px;
    width: 320px;
    font-family: "Crimson Text", Georgia, serif;
    font-style: italic;
    font-size: 23px;
    line-height: 32px;
    color: var(--ink-dark);
    text-align: right;
    white-space: nowrap;
  }
</style>
</head>
<body>
  <main class="spread">
    <section class="page-left">
      <div class="hero-photo" role="img" aria-label="Photo: a couple in deck chairs holding hands on a beach at sunset"></div>
      <div class="story-panel">
        <p class="story-text">
          <span class="story-line">Lorem Ipsum is simply dummy text of the printing and typesetting industry. Lorem Ipsum</span>
          <span class="story-line">has been the industry's standard dummy text ever since the 1500s, when an unknown</span>
          <span class="story-line">printer took a galley of type and scrambled it to make a type specimen book. It has</span>
          <span class="story-line">survived not only five centuries, but also the leap into electronic typesetting, remaining</span>
          <span class="story-line">essentially unchanged. It was popularised in the 1960s with the release of Typeloft sheets</span>
          <span class="story-line">containing Lorem Ipsum passages, and more recently with desktop publishing software</span>
          <span class="story-line story-line--last">like Quillset Composer including versions of Lorem Ipsum.</span>
        </p>
      </div>
    </section>

    <section class="page-right">
      <div class="scenery-photo" role="img" aria-label="Photo: a canal city waterfront with boats and mooring posts on turquoise water"></div>

      <svg class="title-rules" width="224" height="92" viewBox="0 0 224 92" aria-hidden="true">
        <line x1="0" y1="4" x2="224" y2="4" stroke="var(--ornament)" stroke-width="1"/>
        <line x1="0" y1="68" x2="224" y2="68" stroke="var(--ornament)" stroke-width="1"/>
      </svg>
      <h1 class="album-title">Travel Album</h1>

      <svg class="section-rule section-rule--top" width="257" height="10" viewBox="0 0 257 10" aria-hidden="true">
        <line x1="0" y1="8" x2="257" y2="8" stroke="var(--ornament)" stroke-width="2"/>
      </svg>

      <div class="photo-strip">
        <div class="strip-photo strip-photo--girl" role="img" aria-label="Photo: a smiling child lying in a green hammock"></div>
        <div class="strip-photo strip-photo--woman" role="img" aria-label="Photo: a cheerful woman raising her arms outdoors"></div>
        <div class="strip-photo strip-photo--couple" role="img" aria-label="Photo: an older couple relaxing in deck chairs"></div>
      </div>

      <svg class="section-rule section-rule--bottom" width="257" height="10" viewBox="0 0 257 10" aria-hidden="true">
        <line x1="0" y1="2" x2="257" y2="2" stroke="var(--ornament)" stroke-width="2"/>
      </svg>

      <p class="caption">Lorem Ipsum is simply<br>dummy text of the printing<br>and typesetting industry.</p>
    </section>
  </main>
</body>
</html>
```